Award-winnning Estate Agent needs a premium version of their 'For Sale' board design

We need a premium option for our 'For Sale' board design. We have a standard board that is attached to this brief, but were are looking to have a premium design version that we will use when selling exclusive properties. Our company name is Harbour Lane Estates and the name for this is exclusive selection is: 'The Harbour Collection'. The design needs to work with our current brand, but have a distinctive PREMIUM feel to it. I have uploaded the barnd guidelines and also some of the exisisting logo variations. We do NOT need a new logo but feel free to play around with colours, fonts, sizes etc. for the sign.

Target Market(s)

Property buyers & house hunters

Industry/Entity Type

Real Estate - Residential Property

Font styles to use
Sans Serif

Requirements
Must have
• A premium fee, must be square design, must be easy to read when driving past the sign
Nice to have
• I'm open ot ideas

```html
<!DOCTYPE html>
<html lang="en">
<head>
<meta charset="utf-8">
<title>Harbour Lane Estates – The Harbour Collection For Sale Board</title>
<link href="https://fonts.googleapis.com/css2?family=Archivo+Black&family=Arimo:ital,wght@0,400;0,700;1,700&display=swap" rel="stylesheet">
<style>
  :root {
    --navy: #2b3990;
    --sky: #27a8e0;
    --ocean: #1a75bc;
    --stripe-dark: #24408f;
    --stripe-light: #1f7fc8;
    --ornament: #2aa3e0;
    --white: #ffffff;
  }
  html, body {
    margin: 0;
    padding: 0;
    width: 1200px;
    height: 1200px;
    overflow: hidden;
    background: var(--white);
  }
  .board {
    position: relative;
    width: 1200px;
    height: 1200px;
    overflow: hidden;
    font-family: "Arimo", Arial, sans-serif;
    color: var(--white);
  }
  .band { position: absolute; left: 0; width: 1200px; }
  .band--brand { top: 0; height: 535px; background: var(--navy); }
  .band--offer { top: 538px; height: 504px; background: var(--sky); }
  .band--web { top: 1046px; height: 154px; background: var(--ocean); }

  .corner-ornament, .divider-ornament {
    position: absolute;
    background: var(--ornament);
    border-radius: 12px;
  }
  .corner-ornament--tl-h { left: 58px; top: 52px; width: 235px; height: 36px; }
  .corner-ornament--tl-v { left: 60px; top: 102px; width: 36px; height: 204px; }
  .corner-ornament--tr-h { left: 907px; top: 52px; width: 235px; height: 36px; }
  .corner-ornament--tr-v { left: 1104px; top: 102px; width: 36px; height: 204px; }
  .divider-ornament { background: var(--white); height: 26px; width: 172px; left: 514px; }
  .divider-ornament--top { top: 523px; }
  .divider-ornament--bottom { top: 1031px; }

  .brand-mark {
    position: absolute;
    left: 500px;
    top: 130px;
    width: 200px;
    height: 200px;
    box-sizing: border-box;
    border: 10px solid var(--white);
    border-radius: 50%;
  }
  .brand-name {
    position: absolute;
    left: 0; width: 1200px;
    top: 392px;
    margin: 0;
    text-align: center;
    font-weight: 700;
    font-size: 74px;
    line-height: 1;
    letter-spacing: -1px;
    white-space: nowrap;
  }
  .collection-name {
    position: absolute;
    left: 0; width: 1200px;
    top: 578px;
    margin: 0;
    text-align: center;
    font-weight: 700;
    font-style: italic;
    font-size: 84px;
    line-height: 1;
    white-space: nowrap;
  }
  .for-sale {
    position: absolute;
    left: 0; top: 660px;
    width: 1200px; height: 200px;
  }
  .for-sale text {
    font-family: "Archivo Black", "Arial Black", sans-serif;
    font-size: 212px;
  }
  .phone {
    position: absolute;
    left: 0; width: 1200px;
    top: 846px;
    margin: 0;
    text-align: center;
    font-weight: 700;
    font-size: 176px;
    line-height: 1;
    letter-spacing: -3px;
    white-space: nowrap;
    text-shadow: -5px 4px 0 var(--navy);
  }
  .website {
    position: absolute;
    left: 0; width: 1200px;
    top: 1084px;
    margin: 0;
    text-align: center;
    font-weight: 400;
    font-size: 76px;
    line-height: 1;
    white-space: nowrap;
  }
</style>
</head>
<body>
<main class="board">
  <div class="band band--brand"></div>
  <div class="band band--offer"></div>
  <div class="band band--web"></div>

  <div class="corner-ornament corner-ornament--tl-h" role="img" aria-label="Decorative drop ornament border, top left"></div>
  <div class="corner-ornament corner-ornament--tl-v" role="img" aria-label="Decorative drop ornament border, left side"></div>
  <div class="corner-ornament corner-ornament--tr-h" role="img" aria-label="Decorative drop ornament border, top right"></div>
  <div class="corner-ornament corner-ornament--tr-v" role="img" aria-label="Decorative drop ornament border, right side"></div>
  <div class="divider-ornament divider-ornament--top" role="img" aria-label="Decorative divider ornament"></div>
  <div class="divider-ornament divider-ornament--bottom" role="img" aria-label="Decorative divider ornament"></div>

  <div class="brand-mark"></div>
  <h1 class="brand-name">Harbour Lane Estates</h1>

  <h2 class="collection-name">The Harbour Collection</h2>

  <svg class="for-sale" viewBox="0 0 1200 200" aria-label="For Sale">
    <defs>
      <pattern id="sale-stripes" patternUnits="userSpaceOnUse" width="8" height="9">
        <rect width="8" height="9" fill="var(--stripe-light)"/>
        <rect width="8" height="4" fill="var(--stripe-dark)"/>
      </pattern>
    </defs>
    <text x="66" y="175" textLength="1070" lengthAdjust="spacingAndGlyphs" fill="var(--navy)">FOR SALE</text>
    <text x="72" y="170" textLength="1070" lengthAdjust="spacingAndGlyphs" fill="url(#sale-stripes)" stroke="var(--white)" stroke-width="5" paint-order="stroke">FOR SALE</text>
  </svg>

  <p class="phone">01632 960481</p>

  <p class="website">www.harbourlaneestates.co.uk</p>
</main>
</body>
</html>
```